Business Card

THIS IS THE CARD INFORMATION
DEVELOPMENT I FINANCING I PROPERTY MANAGEMENT
DANIEL OSTRAVEN
3182 NW 97th Avenue
Palm Hollow, FL 33418
Telephone I 877.452.6184
Facsimile I 877.452.6127
Industry/Entity Type
Business

```html
<!DOCTYPE html>
<html lang="en">
<head>
<meta charset="utf-8">
<title>Ostraven Paz &amp; Company – Business Card</title>
<link href="https://fonts.googleapis.com/css2?family=Source+Sans+3:wght@400;700&display=swap" rel="stylesheet">
<style>
  :root {
    --stage: #2a2728;
    --plum-light: #a0267f;
    --plum-dark: #6a1f5e;
    --plum-deep: #4a1040;
    --accent: #8a1a78;
    --paper: #ffffff;
    --ink: #1a1a1a;
  }
  * { box-sizing: border-box; margin: 0; padding: 0; }
  html, body { width: 1200px; height: 1000px; overflow: hidden; }
  body {
    background: var(--stage);
    font-family: "Source Sans 3", "Myriad Pro", Arial, sans-serif;
    position: relative;
  }
  .card {
    position: absolute;
    width: 722px;
    height: 425px;
    background: var(--paper);
    overflow: hidden;
  }
  .card--back { left: 254px; top: 46px; }
  .card--front { left: 255px; top: 512px; }
  .band {
    position: absolute;
    left: 0; top: 0; right: 0;
    height: 255px;
    background: linear-gradient(100deg, var(--plum-light) 0%, var(--plum-dark) 100%);
  }
  .card--front .band { height: 256px; }
  .abs { position: absolute; white-space: nowrap; }

  /* contact side */
  .services-line { left: 32px; top: 27px; font-size: 18.5px; color: var(--paper); letter-spacing: 0.3px; }
  .services-line .sep { font-size: 24px; margin: 0 2px; }
  .holder-name { left: 35px; top: 68px; font-size: 26px; font-weight: 400; color: var(--paper); letter-spacing: 0.6px; }
  .address { left: 35px; top: 113px; font-size: 16.5px; line-height: 23px; color: var(--paper); letter-spacing: 0.2px; }
  .contact { left: 35px; top: 167px; font-size: 16.5px; line-height: 20.5px; color: var(--paper); }
  .contact div { display: block; }
  .contact dt { display: inline-block; width: 82px; }
  .contact dd { display: inline; }
  .brand-mini { left: 34px; top: 313px; display: flex; align-items: center; gap: 10px; }
  .brand-mini .dot { width: 60px; height: 60px; border-radius: 50%; background: var(--accent); }
  .brand-mini .name { color: var(--accent); font-weight: 700; line-height: 0.9; }
  .brand-mini .name .main { display: block; font-size: 36px; }
  .brand-mini .name .sub { display: block; font-size: 17px; text-align: right; }
  .seal { position: absolute; left: 436px; top: 143px; }

  /* brand side */
  .brand-large { left: 65px; top: 90px; display: flex; align-items: center; gap: 22px; }
  .brand-large .dot { width: 94px; height: 94px; border-radius: 50%; background: var(--paper); }
  .brand-large .name { color: var(--paper); font-weight: 700; line-height: 0.9; }
  .brand-large .name .main { display: block; font-size: 70px; letter-spacing: 0.5px; }
  .brand-large .name .sub { display: block; font-size: 30px; text-align: right; }
  .services-row { left: 74px; top: 279px; font-size: 21px; color: var(--ink); letter-spacing: 0.2px; }
  .services-row .bullet { color: var(--accent); margin: 0 18px; }
  .website { right: 101px; top: 328px; font-size: 24px; color: var(--accent); }
</style>
</head>
<body>

<section class="card card--back" aria-label="Business card, contact side">
  <div class="band"></div>
  <p class="abs services-line">DEVELOPMENT<span class="sep">/</span>FINANCING<span class="sep">/</span> PROPERTY MANAGEMENT</p>
  <h1 class="abs holder-name">DANIEL OSTRAVEN</h1>
  <p class="abs address">3182 NW 97th Avenue<br>Palm Hollow, FL 33418</p>
  <dl class="abs contact">
    <div><dt>Telephone :</dt><dd>877.452.6184</dd></div>
    <div><dt>Facsimile</dt><dd>: 877.452.6127</dd></div>
    <div><dt>Email</dt><dd>: dostraven@ostravenpazandco.com</dd></div>
  </dl>
  <div class="abs brand-mini">
    <span class="dot"></span>
    <span class="name"><span class="main">OSTRAVEN PAZ</span><span class="sub">&amp; COMPANY</span></span>
  </div>
  <svg class="seal" width="240" height="240" viewBox="0 0 240 240" aria-hidden="true">
    <circle cx="120" cy="120" r="119" fill="var(--plum-deep)"/>
  </svg>
</section>

<section class="card card--front" aria-label="Business card, brand side">
  <div class="band"></div>
  <div class="abs brand-large">
    <span class="dot"></span>
    <span class="name"><span class="main">OSTRAVEN PAZ</span><span class="sub">&amp; COMPANY</span></span>
  </div>
  <p class="abs services-row">DEVELOPMENT<span class="bullet">•</span>FINANCING<span class="bullet">•</span>PROPERTY MANAGEMENT</p>
  <p class="abs website">www.ostravenpazandco.com</p>
</section>

</body>
</html>
```